Help us Create Excitement with a Food To Go Web Site Menu

We are seeking a design that can serve as a template for a Wordpress based website. The template will present the name (BrimBowl), present the menu items with price details, and contact details. The final design should NOT have the Mingle Kerb Eats subtitle anywhere in the site.
Our plan is to have the menu with basic graphic elements with the options to link to images/pictures of the menu item (perhaps linked via Instagram or something like that if possible).
Updates

Target Market(s)

Home dining menu intended to offer perspective customers an understanding of what they will be enjoying.

Contact Information for Business Card

BrimBowl logo (without the Mingle Kerb Eats tag line included)
hi@brimbowl.com.au
Phone: XXXX XXX XXX (to be provided)

Coding

Coded - Design and coding required

Number of Pages Required

2 page

Requirements
Must have
• A bold and colourful presence that is also on the playful side.

A clearly readable menu layout that doesn't feel small based on the limited number of items that we offer at this time.
Nice to have
• A playful semi-graffiti based feel would be nice to convey a sense of playfulness.
Should not have
• The design should not have an overly Asian feel to it.

It appears many people are misreading the brief so I am adding this point to clarify one of the design requirements.
-- The final design should NOT have the Mingle Kerb Eats subtitle anywhere in the site, including the logo.

```html
<!DOCTYPE html>
<html lang="en">
<head>
<meta charset="utf-8">
<title>BrimBowl</title>
<link rel="stylesheet" href="https://fonts.googleapis.com/css2?family=Poppins:wght@400;500;600;700;800&family=Open+Sans:wght@400;600;700&display=swap">
<style>
:root{
  --red:#e3000f;
  --deep-red:#7d0c0c;
  --ink:#1b1b1d;
  --text:#2b2b2b;
  --white:#ffffff;
  --grey-band:#e5e5e5;
  --grey-edge:#b5b5b5;
  --footer:#1b1b1d;
  --footer-text:#b9b9b9;
  --insta:#4a6b94;
}
*{box-sizing:border-box;margin:0;padding:0}
html,body{width:1200px;height:3486px;overflow:hidden;background:var(--white)}
body{position:relative;font-family:"Open Sans",sans-serif;color:var(--text)}
.abs{position:absolute}
.heading{font-family:"Poppins",sans-serif;font-weight:700;color:var(--red);font-size:43px;line-height:1}
.btn{position:absolute;display:flex;align-items:center;justify-content:center;font-family:"Poppins",sans-serif;font-size:14px;font-weight:500;border-radius:20px}
.btn-dark{background:var(--ink);color:var(--white)}
.btn-outline{border:1.5px solid var(--ink);color:var(--ink);background:transparent}

/* header */
.site-header{position:absolute;left:0;top:0;width:1200px;height:131px;background:var(--white)}
.brand{position:absolute;left:145px;top:36px;font-family:"Poppins",sans-serif;font-weight:800;font-size:42px;color:var(--ink);letter-spacing:-1px}
.contact-line{position:absolute;right:145px;top:22px;display:flex;align-items:center;gap:8px;font-family:"Poppins",sans-serif;font-size:22px;font-weight:600;color:var(--ink)}
.contact-line a{color:var(--deep-red);font-weight:500;text-decoration:none}
.main-nav{position:absolute;right:145px;top:76px;display:flex;gap:37px;font-family:"Poppins",sans-serif;font-size:17px;color:var(--ink)}
.main-nav .active{color:var(--red)}

/* hero */
.hero{position:absolute;left:0;top:131px;width:1200px;height:690px;overflow:hidden}
.hero-photo{position:absolute;inset:0;background:radial-gradient(ellipse 360px 330px at 50% 40%,#d39a52 0%,#b7854f 35%,#9a9295 70%,#8d8c92 100%)}
.hero-title{position:absolute;left:0;width:1200px;top:208px;text-align:center;font-family:"Poppins",sans-serif;font-weight:700;font-size:50px;line-height:64px;color:#111;text-shadow:0 0 12px rgba(255,255,255,.6)}
.hero-arrow{position:absolute;top:246px;width:45px;height:45px;border-radius:50%;background:var(--ink);display:flex;align-items:center;justify-content:center}
.hero-edge{position:absolute;left:0;top:0}

/* welcome */
.welcome-title{position:absolute;left:145px;top:893px}
.welcome-copy{position:absolute;left:145px;top:952px;width:415px;font-size:13.5px;line-height:25.6px;color:var(--text)}
.welcome-photo{position:absolute;left:656px;top:897px;width:400px;height:292px;border:6px solid #0d0d0d;background:linear-gradient(135deg,#3b4650 0%,#6a5a44 40%,#394452 70%,#2d3640 100%);transform:rotate(-.4deg)}

/* food */
.food-band{position:absolute;left:0;top:1277px;width:1200px;height:740px}
.food-title{position:absolute;left:0;width:1200px;top:1354px;text-align:center}
.food-card{position:absolute;top:1419px;width:210px}
.food-photo{position:relative;width:210px;height:209px}
.insta-tag{position:absolute;right:0;bottom:0;width:40px;height:38px;background:var(--insta)}
.food-name{margin-top:12px;font-size:19px;font-weight:700;color:var(--ink);line-height:24px}
.food-name small{font-size:12.5px;font-weight:400}
.food-note{font-size:12.5px;line-height:17px;color:var(--ink)}
.food-price{font-family:"Open Sans",sans-serif;font-weight:700;font-size:21px;color:var(--red);line-height:28px;margin-top:2px}
.food-desc{margin-top:16px;font-size:9.5px;line-height:16px;color:var(--text);height:34px}
.food-desc em{font-style:normal;color:var(--red)}
.food-card .btn{position:relative;width:112px;height:31px;margin-top:8px}

/* gallery */
.gallery-title{position:absolute;left:0;width:1200px;top:2095px;text-align:center}
.tile{position:absolute}

/* location */
.location{position:absolute;left:0;top:2771px;width:1200px;height:715px;background:linear-gradient(180deg,#efefef,#e2e2e2)}
.location-title{position:absolute;left:0;width:1200px;top:2848px;text-align:center}

/* footer */
.footer-edge{position:absolute;left:0;top:3190px}
.footer-links{position:absolute;left:145px;top:3390px;font-size:11.5px;color:var(--footer-text);display:flex;gap:10px}
.copyright{position:absolute;left:145px;top:3422px;font-size:11.5px;color:var(--footer-text)}
.social{position:absolute;top:3404px;width:20px;height:20px;border:2px solid #8e8e8e;border-radius:3px}
</style>
</head>
<body>

<header class="site-header">
  <div class="brand">BrimBowl</div>
  <div class="contact-line">
    <svg width="20" height="15" viewBox="0 0 20 15"><rect x="0" y="0" width="20" height="15" rx="2" fill="#1b1b1d"/><path d="M1 1.5 L10 8.5 L19 1.5" stroke="#fff" stroke-width="1.6" fill="none"/></svg>
    <span>Questions? <a>hi@brimbowl.com.au</a></span>
  </div>
  <nav class="main-nav">
    <span class="active">Home</span><span>Food Items</span><span>Gallery</span><span>About Us</span><span>Contact Us</span>
  </nav>
</header>

<section class="hero">
  <div class="hero-photo" role="img" aria-label="Hand holding a loaded burger wrapped in newspaper against a grey stone background"></div>
  <svg class="hero-edge" width="1200" height="690" viewBox="0 131 1200 690">
    <defs>
      <linearGradient id="heroRed" x1="0" y1="0" x2="0" y2="1">
        <stop offset="0" stop-color="#e3000f" stop-opacity="0"/>
        <stop offset="1" stop-color="#e3000f" stop-opacity=".95"/>
      </linearGradient>
    </defs>
    <rect x="0" y="560" width="1200" height="261" fill="url(#heroRed)"/>
    <polygon points="0,672 77,748 277,667 471,812 599,672 970,781 1103,672 1200,724 1200,821 0,821" fill="#111"/>
    <polygon points="0,684 77,736 277,681 471,800 599,690 970,768 1103,690 1200,738 1200,821 0,821" fill="#fff"/>
  </svg>
  <h1 class="hero-title">Etiam massa elementum<br>bibendum venenatis</h1>
  <div class="hero-arrow" style="left:47px"><svg width="14" height="18" viewBox="0 0 14 18"><path d="M10 2 L3 9 L10 16" stroke="#fff" stroke-width="3" fill="none"/></svg></div>
  <div class="hero-arrow" style="left:1107px"><svg width="14" height="18" viewBox="0 0 14 18"><path d="M4 2 L11 9 L4 16" stroke="#fff" stroke-width="3" fill="none"/></svg></div>
</section>

<section class="welcome">
  <h2 class="heading welcome-title">Welcome to BrimBowl</h2>
  <p class="welcome-copy">Nullam lorem urna, tempus eget mollis dapibus ac sem. Suspendisse gravida ornare erat sed pulvinar. Vestibulum luctus ex in egestas fringilla. Fusce nec leo ac urna pulvinar auctor. Mauris bibendum fringilla velit. Nulla in lorem at massa pellentesque posuere. Nulla tristique posuere molestie. Aliquam erat volutpat. Etiam quis aliquet risus. Duis ornare erat eget magna dapibus, in accumsan quam pharetra. Nam tempus, quam in bibendum vulputate.</p>
  <span class="btn btn-dark" style="left:145px;top:1151px;width:111px;height:38px">Read More</span>
  <div class="welcome-photo" role="img" aria-label="Platter of grilled kebabs, flatbread, salads and dips on a dark table"></div>
</section>

<section class="food">
  <svg class="food-band" width="1200" height="740" viewBox="0 1277 1200 740">
    <polygon points="0,1277 1200,1277 1200,1881 1123,1951 924,1873 731,2016 602,1873 528,1919 461,1873 230,1985 0,1881" fill="#b5b5b5"/>
    <polygon points="0,1277 1200,1277 1200,1873 1123,1937 924,1865 731,2000 602,1865 528,1908 461,1865 230,1972 0,1873" fill="#e5e5e5"/>
  </svg>
  <h2 class="heading food-title">Our Food Items</h2>

  <article class="food-card" style="left:145px">
    <div class="food-photo" role="img" aria-label="Bowl of beef noodle soup with fresh herbs" style="background:radial-gradient(circle at 45% 45%,#d9e3c8 0%,#9fb77a 35%,#6b5236 75%,#3d2e22 100%)"><span class="insta-tag"></span></div>
    <h3 class="food-name">Phở <small>(beef noodle soup)</small></h3>
    <div class="food-price">$14</div>
    <p class="food-desc">Just like Ba (Grandma) used to make. Our Pho takes 12 hours to make. <em>More</em></p>
    <span class="btn btn-outline">Add to order</span>
  </article>

  <article class="food-card" style="left:379px">
    <div class="food-photo" role="img" aria-label="Hands rolling fresh egg rolls on banana leaves" style="background:linear-gradient(150deg,#3e5a2a 0%,#7d8a6a 45%,#9d8e8a 70%,#2f3b25 100%)"><span class="insta-tag"></span></div>
    <h3 class="food-name">Egg Rolls <small>(life changing)</small></h3>
    <div class="food-price">$10 for 10</div>
    <p class="food-desc">Just like Ba (Grandma) used to make. Our Pho takes 12 hours to make. <em>More</em></p>
    <span class="btn btn-outline">Add to order</span>
  </article>

  <article class="food-card" style="left:612px">
    <div class="food-photo" role="img" aria-label="Spoonful of thick crab soup" style="background:radial-gradient(circle at 50% 40%,#e8ddc9 0%,#c9a36a 45%,#b57a3a 75%,#5a3b1e 100%)"><span class="insta-tag"></span></div>
    <h3 class="food-name">Crab Soup</h3>
    <div class="food-note">(mmm so good, so fresh)</div>
    <div class="food-price">$Market Price</div>
    <p class="food-desc">Just like Ba (Grandma) used to make. Our Pho takes 12 hours to make. <em>More</em></p>
    <span class="btn btn-outline">Add to order</span>
  </article>

  <article class="food-card" style="left:846px">
    <div class="food-photo" role="img" aria-label="Stacked tuna salad sandwich on white" style="background:radial-gradient(ellipse 90px 60px at 50% 55%,#d8b98e 0%,#efe4d4 60%,#ffffff 100%)"><span class="insta-tag"></span></div>
    <h3 class="food-name">Tuna Salad Sandwich</h3>
    <div class="food-note">(sweet, sour, and tangy)</div>
    <div class="food-price">$9</div>
    <p class="food-desc">Just like Ba (Grandma) used to make. Our Pho takes 12 hours to make. <em>More</em></p>
    <span class="btn btn-outline">Add to order</span>
  </article>
</section>

<section class="gallery">
  <h2 class="heading gallery-title">Gallery</h2>
  <div class="tile" role="img" aria-label="Plate of tacos with lime on dark slate" style="left:145px;top:2161px;width:296px;height:207px;background:radial-gradient(circle at 55% 50%,#a8905a 0%,#5e6a3e 35%,#2b2e33 70%)"></div>
  <div class="tile" role="img" aria-label="Burgers served on paper at an outdoor table" style="left:452px;top:2161px;width:296px;height:207px;background:linear-gradient(180deg,#7d8990 0%,#b48654 50%,#6b4a2d 100%)"></div>
  <div class="tile" role="img" aria-label="Paper cones of fries and fried seafood" style="left:759px;top:2161px;width:296px;height:207px;background:linear-gradient(160deg,#8b96a3 0%,#d9a456 50%,#efe7de 100%)"></div>
  <div class="tile" role="img" aria-label="Street food vendor adding sauce to a falafel wrap" style="left:145px;top:2377px;width:450px;height:255px;background:linear-gradient(120deg,#9aa0a6 0%,#6a5844 45%,#d7c3a4 75%,#3a332c 100%)"></div>
  <div class="tile" role="img" aria-label="Hands holding a stuffed sandwich in a paper box" style="left:605px;top:2377px;width:450px;height:255px;background:radial-gradient(circle at 50% 45%,#c9a070 0%,#8a5a36 40%,#2a2624 80%)"></div>
  <span class="btn btn-dark" style="left:544px;top:2653px;width:112px;height:38px">View All</span>
</section>

<section class="location" role="img" aria-label="Street map of the city around the shop"></section>
<h2 class="heading location-title">Location</h2>
<svg class="abs" style="left:595px;top:2958px" width="30" height="46" viewBox="0 0 30 46">
  <path d="M15 0 C6.7 0 0 6.7 0 15 C0 26 15 46 15 46 C15 46 30 26 30 15 C30 6.7 23.3 0 15 0Z" fill="#e3000f"/>
  <circle cx="15" cy="15" r="6" fill="#fff"/>
</svg>

<footer>
  <svg class="footer-edge" width="1200" height="296" viewBox="0 3190 1200 296">
    <polygon points="0,3220 230,3315 461,3207 514,3234 731,3349 924,3207 1123,3288 1200,3234 1200,3486 0,3486" fill="#e3000f"/>
    <polygon points="0,3232 230,3330 461,3220 514,3248 731,3364 924,3222 1123,3303 1200,3250 1200,3486 0,3486" fill="#1b1b1d"/>
  </svg>
  <nav class="footer-links"><span>Home</span><span>|</span><span>Food Items</span><span>|</span><span>Gallery</span><span>|</span><span>About Us</span><span>|</span><span>Contact Us</span></nav>
  <p class="copyright">Copyright ©&nbsp; 2020 &nbsp;BrimBowl.&nbsp; All rights reserved.</p>
  <span class="social" aria-label="Social link" style="left:992px"></span>
  <span class="social" aria-label="Social link" style="left:1035px"></span>
</footer>

</body>
</html>
```